Business Coaching Model and Flow Chart

We need this flowchart, attached, to be updated in a modern and engaging way. This flowchart is the cornerstone of a business coaching class we are running, and will be the main support reference for the people who take the class. We are open to ideas as to how it is presented, but we would like a largely minimalist look that leaves space to be impactful where the key information sites. Our colour scheme is primary red (D51C29), white, grey (333333), black, and secondary green (3C8740). We will also need our logo present (attached).

```html
<!DOCTYPE html>
<html lang="en">
<head>
<meta charset="utf-8">
<title>Groups to Teams – Through Learning Together</title>
<link href="https://fonts.googleapis.com/css2?family=Poppins:wght@400;500;600;700&display=swap" rel="stylesheet">
<style>
:root{
  --red:#d51c29;
  --green:#3c8740;
  --grey:#333333;
  --black:#111111;
  --white:#ffffff;
  --paper:#f7f7f7;
  --soft-pink:#f6d3d7;
  --soft-green:#dfeadf;
}
*{margin:0;padding:0;box-sizing:border-box}
html,body{width:889px;height:1200px;overflow:hidden;background:var(--paper)}
body{font-family:'Poppins',sans-serif;color:var(--grey);position:relative}
.abs{position:absolute}

.brand{position:absolute;left:0;top:0;width:889px;height:143px;text-align:center}
.brand-mark{position:absolute;left:398px;top:20px;width:94px;height:94px;border-radius:50%;background:var(--red)}
.brand-name{position:absolute;left:0;width:100%;top:120px;font-weight:700;font-size:12px;letter-spacing:1px;color:var(--red)}

.title-band{position:absolute;left:0;top:143px;width:889px;height:88px;background:var(--red);text-align:center;color:var(--white)}
.title-band h1{font-weight:700;font-size:31px;line-height:1;margin-top:20px;letter-spacing:.5px}
.title-band p{font-weight:700;font-size:17px;color:#f0c9cc;margin-top:4px}

.flow{position:absolute;left:0;top:0;width:889px;height:1200px;pointer-events:none}

.stage-icon{position:absolute;width:80px;height:80px;border-radius:50%;background:var(--white);box-shadow:4px 6px 10px rgba(0,0,0,.22);display:flex;align-items:center;justify-content:center}
.stage-icon .art{width:44px;height:44px;border-radius:50%;background:radial-gradient(circle at 40% 40%,var(--red) 0 40%,var(--green) 41% 100%)}

.step-no{position:absolute;width:25px;height:25px;border-radius:50%;background:var(--grey);border:2px solid var(--white);box-shadow:0 0 0 1px var(--grey);color:var(--white);font-weight:700;font-size:13px;display:flex;align-items:center;justify-content:center}

.stage-pill{position:absolute;height:34px;background:var(--green);color:var(--white);border-radius:10px;padding:0 12px;display:flex;flex-direction:column;justify-content:center;line-height:1.05}
.stage-pill::before{content:"";position:absolute;left:-12px;top:50%;transform:translateY(-50%);border:9px solid transparent;border-right:12px solid var(--green);border-left:0}
.stage-pill strong{font-weight:700;font-size:15px}
.stage-pill span{font-weight:400;font-size:11px}
.stage-pill.single{align-items:center}
.stage-pill.single strong{font-size:17px}

.points{position:absolute;list-style:none;font-weight:600;font-size:10.5px;color:var(--grey)}
.points li{position:relative;padding-left:13px;line-height:1.15}
.points li::before{content:"";position:absolute;left:0;top:3px;width:7px;height:7px;border-radius:50%;border:1.5px solid var(--black);background:radial-gradient(circle,var(--black) 0 1.5px,transparent 2px)}
.points .sub{list-style:none;font-weight:500;font-size:6.5px;color:#666;padding:1px 0 1px 8px}
.points .sub li{padding-left:7px;line-height:1.55}
.points .sub li::before{width:3px;height:3px;border:0;background:#888;top:3px}

.glow-pink{position:absolute;background:radial-gradient(ellipse at center,var(--soft-pink),rgba(246,211,215,0) 75%)}
.glow-grey{position:absolute;background:radial-gradient(ellipse at center,#ebebeb,rgba(235,235,235,0) 80%)}
.glow-green{position:absolute;background:linear-gradient(90deg,rgba(223,234,223,0),var(--soft-green) 25%,var(--soft-green) 80%,rgba(223,234,223,.5))}

.footer-band{position:absolute;left:0;top:1178px;width:889px;height:22px;background:var(--red)}
</style>
</head>
<body>

<header class="brand">
  <div class="brand-mark"></div>
  <div class="brand-name">LENA MARWICK</div>
</header>

<section class="title-band">
  <h1>GROUPS TO TEAMS</h1>
  <p>THROUGH LEARNING TOGETHER</p>
</section>

<svg class="flow" viewBox="0 0 889 1200" fill="none">
  <g stroke="var(--green)" stroke-width="3.5" stroke-linecap="round" stroke-dasharray="0 8">
    <path d="M374 299 H440"/>
    <path d="M798 296 H840 Q846 296 846 302 V479 Q846 485 840 485 H68 Q62 485 62 491 V541 Q62 547 68 547 H104"/>
    <path d="M466 553 H505"/>
    <path d="M824 552 H840 Q846 552 846 558 V706 Q846 712 840 712 H68 Q62 712 62 718 V767 Q62 773 68 773 H104"/>
    <path d="M446 777 H505"/>
    <path d="M864 780 H871 Q877 780 877 786 V1023 Q877 1029 871 1029 H68 Q62 1029 62 1035 V1093 Q62 1099 68 1099 H110"/>
  </g>
  <g fill="var(--green)">
    <path d="M446 299 l-10 -6 v12z"/>
    <path d="M846 402 l-6 -10 h12z"/>
    <path d="M432 485 l12 -7 v14z"/>
    <path d="M112 547 l-10 -6 v12z"/>
    <path d="M846 632 l-6 -10 h12z"/>
    <path d="M432 712 l12 -7 v14z"/>
    <path d="M112 773 l-10 -6 v12z"/>
    <path d="M490 1029 l12 -7 v14z"/>
    <path d="M118 1099 l-10 -6 v12z"/>
  </g>
</svg>

<!-- Stage 1 -->
<div class="stage-icon" style="left:58px;top:254px"><div class="art" role="img" aria-label="Hand holding a maze icon"></div></div>
<div class="step-no" style="left:153px;top:287px">1</div>
<div class="stage-pill single" style="left:197px;top:282px;width:170px"><strong>PROBLEM</strong></div>
<div class="glow-pink" style="left:139px;top:322px;width:320px;height:140px"></div>
<ul class="points" style="left:190px;top:334px;width:140px">
  <li style="margin-bottom:7px">Under-billing</li>
  <li style="margin-bottom:7px">Staff Retention</li>
  <li style="margin-bottom:7px">Hard To Recruit</li>
  <li style="margin-bottom:7px">Client Complaints</li>
  <li>Staff Stress and Burnout</li>
</ul>
<ul class="points" style="left:330px;top:334px;width:115px">
  <li style="margin-bottom:7px">Conflict</li>
  <li style="margin-bottom:7px">Funding Constant Change</li>
  <li>Limited In Best Practice</li>
</ul>

<!-- Stage 2 -->
<div class="stage-icon" style="left:451px;top:254px"><div class="art" role="img" aria-label="Person with question mark and bar chart icon"></div></div>
<div class="step-no" style="left:545px;top:287px">2</div>
<div class="stage-pill" style="left:588px;top:280px;width:205px"><strong>Clarify Challenges</strong><span style="font-size:13px">(Diagnostics)</span></div>
<div class="glow-grey" style="left:575px;top:320px;width:230px;height:150px"></div>
<ul class="points" style="left:619px;top:326px;width:180px">
  <li style="margin-bottom:6px">Scoping</li>
  <li style="margin-bottom:6px">Interviews</li>
  <li style="margin-bottom:6px">Group Reflection</li>
  <li style="margin-bottom:6px">Opinion Surveys</li>
  <li>Certified Assessments
    <ul class="sub">
      <li>Personality Styles</li>
      <li>Work Preference</li>
      <li>Strengths &amp; Values</li>
      <li>Trust</li>
      <li>360</li>
    </ul>
  </li>
</ul>

<!-- Stage 3 -->
<div class="stage-icon" style="left:116px;top:507px"><div class="art" role="img" aria-label="Strategy board on an easel icon"></div></div>
<div class="step-no" style="left:210px;top:540px">3</div>
<div class="stage-pill" style="left:247px;top:534px;width:214px"><strong>Planning for success</strong><span>(Make a Plan)</span></div>
<div class="glow-grey" style="left:240px;top:580px;width:240px;height:100px"></div>
<ul class="points" style="left:272px;top:596px;width:200px">
  <li style="margin-bottom:7px">Team Data Analysis Workshop</li>
  <li style="margin-bottom:7px">Individual Development Plan</li>
  <li style="margin-bottom:7px">Team Development Plan</li>
  <li>Organizational Plan</li>
</ul>

<!-- Stage 4 -->
<div class="stage-icon" style="left:511px;top:507px"><div class="art" role="img" aria-label="Gear and wrench icon"></div></div>
<div class="step-no" style="left:605px;top:540px">4</div>
<div class="stage-pill" style="left:641px;top:534px;width:178px"><strong>Learn The Tools</strong><span>(Workshops)</span></div>
<div class="glow-grey" style="left:630px;top:578px;width:200px;height:125px"></div>
<ul class="points" style="left:650px;top:585px;width:180px">
  <li>Foundation Workshops
    <ul class="sub">
      <li>Difficult Conversations</li>
      <li>Giving &amp; Receiving Feedback</li>
      <li>Values Alignment</li>
      <li>Shared Purpose</li>
      <li>Ways Of Working</li>
      <li>Diversity</li>
      <li>Well-being</li>
      <li>Time Management</li>
    </ul>
  </li>
  <li>Customized Workshops</li>
</ul>

<!-- Stage 5 -->
<div class="stage-icon" style="left:116px;top:733px"><div class="art" role="img" aria-label="Person working at a laptop icon"></div></div>
<div class="step-no" style="left:209px;top:766px">5</div>
<div class="stage-pill" style="left:247px;top:760px;width:194px"><strong>Doing</strong><span>(Mastering the Tools)</span></div>
<div class="glow-grey" style="left:240px;top:805px;width:230px;height:120px"></div>
<ul class="points" style="left:268px;top:818px;width:180px">
  <li style="margin-bottom:7px">Group Coaching</li>
  <li style="margin-bottom:7px">Team Coaching</li>
  <li style="margin-bottom:7px">Individual Coaching</li>
  <li style="margin-bottom:7px">Peer Learning</li>
  <li>Lunch ‘N Learn</li>
</ul>

<!-- Stage 6 -->
<div class="stage-icon" style="left:511px;top:733px"><div class="art" role="img" aria-label="Connected stars icon"></div></div>
<div class="step-no" style="left:604px;top:766px">6</div>
<div class="stage-pill single" style="left:647px;top:762px;width:211px"><strong>Reflect-Adapt-Embed</strong></div>
<div class="glow-grey" style="left:640px;top:800px;width:230px;height:215px"></div>
<ul class="points" style="left:663px;top:807px;width:205px">
  <li style="margin-bottom:7px">Culture Committee</li>
  <li style="margin-bottom:7px">Embedding Workshop</li>
  <li style="margin-bottom:7px">Culture Collateral</li>
  <li style="margin-bottom:7px">WOW Manifesto</li>
  <li style="margin-bottom:7px">Leadership Team Coaching</li>
  <li style="margin-bottom:7px">Measure ROI</li>
  <li style="margin-bottom:7px">Review Success</li>
  <li style="margin-bottom:7px">Evaluation Surveys</li>
  <li style="margin-bottom:7px">Temperature Checks</li>
  <li style="margin-bottom:7px">Recruit To Suit</li>
  <li>Future Proofing - What Next?</li>
</ul>

<!-- Stage 7 -->
<div class="glow-green" style="left:397px;top:1063px;width:492px;height:115px"></div>
<div class="stage-icon" style="left:123px;top:1059px"><div class="art" role="img" aria-label="Light bulb with puzzle piece icon"></div></div>
<div class="step-no" style="left:216px;top:1092px">7</div>
<div class="stage-pill single" style="left:261px;top:1083px;width:170px"><strong>SOLUTION</strong></div>
<ul class="points" style="left:448px;top:1086px;width:180px">
  <li style="margin-bottom:7px">Self Awareness &amp; Ownership</li>
  <li style="margin-bottom:7px">Partnership</li>
  <li style="margin-bottom:7px">Great Place To Work</li>
  <li>Growth Mindset</li>
</ul>
<ul class="points" style="left:645px;top:1086px;width:200px">
  <li style="margin-bottom:7px">Coach Approaching Culture</li>
  <li style="margin-bottom:7px">Feedback Culture</li>
  <li style="margin-bottom:7px">Way To Manage Conflict</li>
  <li>Best Practice Communication Skills</li>
</ul>

<div class="footer-band"></div>
</body>
</html>
```